Wordpress Design Project - Basketball Tournament

We need a wordpress design with 3 unique pages for a youth basketball tournament called The Rumble by the Bay. It will take place on April 20-22. The tournament is hosted by Summit Hoops a non-profit youth basketball organization in Southern California.

We really like the www.tallpinecourts.example website. We are open to ideas about colors. I would like to see bold graphics to that bleed to the edge of the website. Ultimately the website must have a simple and sleek design.

We plan on having the following webpages. Many of these webpages can use the same design, and we can just change the content.

About
Location
Register
Teams - a list of all teams that are participating and divisions (Elite, Open, HS, Girls, etc)
Media
NIAB Coaches
Club/HS Coaches - This is where we provide info on how to get NIAB certified and how to load the roster online
Schedule
Accommodations

Other websites I like include:
http://www.haroldpwinton.example/
www.velorafinal32.example

This contest is for design only.  If you wish to do the code as well, please provide a separate quote for that.  Please include how long it will take to do the coding.  I will give preference to submissions that have the lowest total price for the design and code.

Thank you,
Derek

All designs must state "NIAB Certified".  This must be prominently displayed.

Target Market(s)

Basketball coaches are our primary target market. Most of the coaches are between 25-45 years old and African-American.

Industry/Entity Type

Non-Profit

Requirements
Must have
• a box or column that will display pictures and/or videos.
Nice to have
• It would be nice to have a

```html
<!DOCTYPE html>
<html lang="en">
<head>
<meta charset="utf-8">
<title>The Rumble by the Bay</title>
<link rel="stylesheet" href="https://fonts.googleapis.com/css2?family=Open+Sans:wght@400;600;700;800&family=Oswald:wght@500;600&display=swap">
<style>
  :root {
    --black: #0b0b0b;
    --ink: #161616;
    --panel: #3a3a3a;
    --panel-dark: #2c2c2c;
    --orange: #f38a1d;
    --orange-dark: #c9650a;
    --date-text: #3a220c;
    --bar-light: #e9e9e9;
    --bar-mid: #bdbdbd;
    --white: #ffffff;
    --muted: #d8d8d8;
    --about-bg: rgba(232, 232, 232, 0.96);
  }
  * { box-sizing: border-box; margin: 0; padding: 0; }
  html, body { width: 911px; height: 1200px; overflow: hidden; background: var(--white); }
  body { position: relative; font-family: "Open Sans", Arial, sans-serif; }
  .abs { position: absolute; }

  /* header */
  .masthead { left: 0; top: 0; width: 911px; height: 155px; background: radial-gradient(ellipse at 50% 0%, #2a2a2a, var(--black) 70%); }
  .masthead-bar { left: 0; top: 38px; width: 911px; height: 74px; background: linear-gradient(var(--bar-light), #d4d4d4 60%, var(--bar-mid)); box-shadow: 0 3px 6px rgba(0,0,0,.6); }
  .brand-badge { left: 106px; top: 6px; width: 160px; height: 148px; border-radius: 50%; background: var(--ink); display: flex; align-items: center; justify-content: center; text-align: center; }
  .brand-name { font-family: "Oswald", sans-serif; font-weight: 600; font-size: 21px; line-height: 1.1; color: var(--white); text-transform: uppercase; width: 120px; }
  .certified { left: 520px; top: 62px; width: 150px; text-align: right; font-family: "Oswald", sans-serif; font-weight: 600; font-size: 19px; line-height: 26px; color: var(--ink); text-transform: uppercase; }
  .social { top: 58px; width: 33px; height: 33px; border-radius: 4px; background: linear-gradient(#3c3c3c, #101010); box-shadow: 0 1px 3px rgba(0,0,0,.6); border: 1px solid #555; }

  /* hero */
  .hero-band { left: 0; top: 155px; width: 911px; height: 296px; background: var(--black); }
  .hero-slide { left: 99px; top: 155px; width: 713px; height: 279px; background: linear-gradient(90deg, #3a4f86 0%, #8b8c99 30%, #c8c4c2 42%, #9c2a24 62%, #b32a22 80%, #2f47a0 100%); }
  .hero-headline { left: 482px; top: 238px; font-weight: 800; font-size: 45px; line-height: 44px; color: var(--white); text-shadow: 2px 2px 4px rgba(0,0,0,.55); letter-spacing: .6px; }
  .slide-arrow { top: 275px; }

  /* nav */
  .main-nav { left: 0; top: 451px; width: 911px; height: 42px; background: linear-gradient(#3b3b3b, #1a1a1a); border-top: 2px solid #8a5a26; box-shadow: 0 2px 5px rgba(0,0,0,.5); display: flex; align-items: center; padding-left: 99px; }
  .main-nav a { font-size: 12px; color: var(--muted); text-decoration: none; padding: 0 9.5px; border-left: 1px solid #555; line-height: 14px; }
  .main-nav a:first-child { border-left: 0; padding-left: 0; color: var(--orange); font-weight: 600; }

  /* content panel */
  .content-panel { left: 99px; top: 493px; width: 713px; height: 470px; background: radial-gradient(ellipse at 40% 40%, #474747, var(--panel) 60%, var(--panel-dark)); }
  .section-title { font-family: "Oswald", sans-serif; font-weight: 600; font-size: 23px; line-height: 1; color: var(--white); text-transform: uppercase; text-shadow: 1px 1px 2px #000; }

  .event-card { left: 118px; width: 452px; height: 78px; background: linear-gradient(#2b2b2b, #121212); border: 1px solid #555; border-radius: 3px; box-shadow: 0 2px 4px rgba(0,0,0,.6); }
  .event-date { left: 138px; width: 74px; height: 96px; background: linear-gradient(90deg, var(--orange-dark), var(--orange) 30%, #f7a043 70%, var(--orange-dark)); text-align: center; color: var(--date-text); box-shadow: 0 2px 4px rgba(0,0,0,.5); }
  .event-day { display: block; font-weight: 700; font-size: 21px; line-height: 24px; margin-top: 22px; }
  .event-month { display: block; font-family: "Oswald", sans-serif; font-weight: 500; font-size: 22px; line-height: 26px; }
  .event-title { left: 219px; font-family: "Oswald", sans-serif; font-weight: 600; font-size: 14.5px; color: var(--white); white-space: nowrap; }
  .event-text { left: 219px; width: 345px; font-family: Arial, sans-serif; font-size: 9.6px; line-height: 13.5px; color: var(--muted); }

  .btn { display: flex; align-items: center; justify-content: center; height: 20px; border-radius: 3px; background: linear-gradient(#fbab4f, var(--orange) 55%, var(--orange-dark)); color: #2a1706; font-weight: 700; font-size: 11px; text-decoration: none; box-shadow: 0 1px 2px rgba(0,0,0,.6); }

  .media-frame { left: 585px; width: 212px; height: 140px; border: 2px solid #1c1c1c; box-shadow: 0 2px 4px rgba(0,0,0,.6); }
  .photo-frame { top: 548px; background: linear-gradient(90deg, #5c4a46, #b9aea9 40%, #e9e9e9 55%, #6b5e5a 80%, #463a3a); }
  .video-frame { top: 758px; background: linear-gradient(90deg, #3e3a6a, #9a6b45 35%, #d8cfc4 55%, #a0603a 80%, #4a3a30); }

  /* footer */
  .footer { left: 0; top: 960px; width: 911px; height: 240px; background: var(--black); }
  .footer-edge { left: 0; top: 952px; width: 911px; height: 16px; }
  .footer-art { left: 60px; top: 968px; width: 380px; height: 232px; background: radial-gradient(ellipse at 45% 55%, rgba(150,120,60,.35), rgba(120,30,20,.2) 45%, rgba(11,11,11,0) 75%); }
  .about-box { left: 99px; top: 1004px; width: 410px; height: 131px; background: var(--about-bg); border-radius: 3px; box-shadow: 0 2px 6px rgba(0,0,0,.6); }
  .about-title { left: 108px; top: 1010px; color: #1a1a1a; text-shadow: none; }
  .about-photo { left: 107px; top: 1040px; width: 97px; height: 79px; border: 3px solid var(--white); box-shadow: 0 1px 3px rgba(0,0,0,.5); background: linear-gradient(135deg, #3a1e0c, #c8651e 45%, #7a3a12 70%, #cfcfcf); }
  .about-text { left: 220px; top: 1036px; width: 277px; font-family: Arial, sans-serif; font-size: 10.4px; line-height: 13.6px; color: #222; }
  .tweet-title { left: 586px; top: 1001px; }
  .tweet-text { left: 584px; top: 1036px; width: 228px; text-align: center; font-family: Arial, sans-serif; font-size: 10.4px; line-height: 13.8px; color: var(--white); }
  .tweet-text .handle { color: var(--orange); }
  .footer-badge { left: 645px; top: 1105px; width: 68px; height: 68px; border-radius: 50%; background: var(--white); display: flex; align-items: center; justify-content: center; text-align: center; }
  .footer-badge span { font-family: "Oswald", sans-serif; font-weight: 600; font-size: 10px; line-height: 11px; color: var(--ink); text-transform: uppercase; width: 54px; }
  .copyright { left: 700px; top: 1137px; width: 113px; text-align: right; font-family: Arial, sans-serif; font-size: 10px; line-height: 13.5px; color: var(--muted); }
</style>
</head>
<body>

<header>
  <div class="abs masthead"></div>
  <div class="abs masthead-bar"></div>
  <div class="abs brand-badge"><span class="brand-name">The Rumble by the Bay</span></div>
  <p class="abs certified">NIAB Certified</p>
  <a class="abs social" style="left:690px" href="#" aria-label="Social link one"></a>
  <a class="abs social" style="left:734px" href="#" aria-label="Social link two"></a>
  <a class="abs social" style="left:777px" href="#" aria-label="Social link three"></a>
</header>

<section>
  <div class="abs hero-band"></div>
  <div class="abs hero-slide" role="img" aria-label="Photo of a young player dribbling a basketball in front of a seated crowd"></div>
  <h1 class="abs hero-headline">BASKETBALL<br>IS YOUR LIFE</h1>
  <svg class="abs slide-arrow" style="left:60px" width="24" height="42" viewBox="0 0 24 42" aria-label="Previous slide"><polyline points="20,2 4,21 20,40" fill="none" stroke="#8a8a8a" stroke-width="3"/></svg>
  <svg class="abs slide-arrow" style="left:827px" width="24" height="42" viewBox="0 0 24 42" aria-label="Next slide"><polyline points="4,2 20,21 4,40" fill="none" stroke="#8a8a8a" stroke-width="3"/></svg>
</section>

<nav class="abs main-nav">
  <a href="#">About Us</a><a href="#">Location</a><a href="#">Register</a><a href="#">Teams</a><a href="#">Media</a><a href="#">NIAB Coaches</a><a href="#">Club/HS Coaches</a><a href="#">Schedule</a><a href="#">Accommodations</a>
</nav>

<main>
  <div class="abs content-panel"></div>

  <h2 class="abs section-title" style="left:125px;top:515px">Upcoming Events</h2>

  <div class="abs event-card" style="top:562px"></div>
  <div class="abs event-date" style="top:553px"><span class="event-day">22</span><span class="event-month">April</span></div>
  <h3 class="abs event-title" style="top:572px">Lorem ipsum dolor sit amet, consectetuer adipiscing</h3>
  <p class="abs event-text" style="top:596px">fusce suscipit varius mium sociis natoque penatibus et magnis dis parturient montes nascetur ridiculus musulla dui fusce feugiat malesuada odio.</p>
  <a class="abs btn" style="left:487px;top:642px;width:74px" href="#">Read More</a>

  <div class="abs event-card" style="top:689px"></div>
  <div class="abs event-date" style="top:680px"><span class="event-day">21</span><span class="event-month">April</span></div>
  <h3 class="abs event-title" style="top:699px">Lorem ipsum dolor sit amet, consectetuer adipiscing</h3>
  <p class="abs event-text" style="top:723px">fusce suscipit varius mium sociis natoque penatibus et magnis dis parturient montes nascetur ridiculus musulla dui fusce feugiat malesuada odio.</p>
  <a class="abs btn" style="left:487px;top:769px;width:74px" href="#">Read More</a>

  <div class="abs event-card" style="top:820px"></div>
  <div class="abs event-date" style="top:811px"><span class="event-day">20</span><span class="event-month">April</span></div>
  <h3 class="abs event-title" style="top:830px">Lorem ipsum dolor sit amet, consectetuer adipiscing</h3>
  <p class="abs event-text" style="top:854px">fusce suscipit varius mium sociis natoque penatibus et magnis dis parturient montes nascetur ridiculus musulla dui fusce feugiat malesuada odio.</p>
  <a class="abs btn" style="left:487px;top:900px;width:74px" href="#">Read More</a>

  <h2 class="abs section-title" style="left:585px;top:515px">Photo Gallery</h2>
  <div class="abs media-frame photo-frame" role="img" aria-label="Photo of a coach seated courtside watching the game"></div>
  <a class="abs btn" style="left:716px;top:689px;width:74px" href="#">View All</a>

  <h2 class="abs section-title" style="left:585px;top:725px">Video Gallery</h2>
  <div class="abs media-frame video-frame" role="img" aria-label="Video still of two players contesting the ball on court"></div>
  <a class="abs btn" style="left:716px;top:898px;width:74px" href="#">Watch All</a>
</main>

<footer>
  <div class="abs footer"></div>
  <svg class="abs footer-edge" width="911" height="16" viewBox="0 0 911 16" aria-hidden="true"><path d="M0 8 L40 5 L90 9 L150 4 L220 8 L300 5 L380 9 L460 4 L540 8 L620 5 L700 9 L780 4 L850 8 L911 5 L911 16 L0 16 Z" fill="#0b0b0b"/></svg>
  <div class="abs footer-art" role="img" aria-label="Illustrated silhouette of a player dribbling"></div>

  <div class="abs about-box"></div>
  <h2 class="abs section-title about-title">About Us</h2>
  <div class="abs about-photo" role="img" aria-label="Close-up photo of a basketball"></div>
  <p class="abs about-text">Vero eos et accusamus et iusto odio dignissimos ducimus qui blanditiis praesentium voluptatum deleniti atque corrupti quos dolores et quas molestias excepturi sint occaecati cupiditate non provident, similique sunt in culpa qui officia deserunt mollitia animi.</p>
  <a class="abs btn" style="left:423px;top:1103px;width:73px;height:22px" href="#">Read More</a>

  <h2 class="abs section-title tweet-title">Tweet With Us</h2>
  <p class="abs tweet-text">RT <span class="handle">@CoachRendale</span>: RT <span class="handle">@NorthfieldHoops</span>: Marcus Delaney named first-team All-American by National Hoop Writers Guild<br><span class="handle">http://short.example/k7Qm2x</span></p>

  <div class="abs footer-badge"><span>The Rumble by the Bay</span></div>
  <p class="abs copyright">Copyright 2012<br>All Rights Reserved</p>
</footer>

</body>
</html>
```